Meadowlark Learning Growth Partners (MLGP)

This is a professional business card. Logo and picture are a must on the front of the card. I am an educational consultant. I have been consulting for the past three years for a company. I am now opening my own company. My goal for my consulting company is to eventually consult all over America.

Target Market(s)

Educators, schools, professionals

Industry/Entity Type

Consulting

Contact Information for Business Card

Picture/logo on front, simple modern design

Font styles to use
Serif

Colors
85abd2
0355a3
3176b5
cedeed

Requirements
Must have
• picture, logo,
• Odessa Pruitt, Ed.S
• address 5073 Cormorant ridge Dr. Nashville, TN 37940
• Cell:616-555-0148
• Office: 629-555-0172
• www.Mlgpedu.example
• pruittodessa@mailbox.example

```html
<!DOCTYPE html>
<html lang="en">
<head>
<meta charset="utf-8">
<title>Odessa Pruitt – Business Card</title>
<link rel="stylesheet" href="https://fonts.googleapis.com/css2?family=Marcellus&family=Gelasio:wght@600&family=Source+Sans+3:wght@500&display=swap">
<style>
  :root {
    --sky: #85abd2;
    --navy: #0355a3;
    --azure: #3176b5;
    --mist: #cedeed;
    --paper: #eef3fa;
    --band: #a3c1e2;
    --ink-light: #f4f8fd;
  }
  html, body {
    margin: 0;
    padding: 0;
    width: 1200px;
    height: 686px;
    overflow: hidden;
    background: var(--paper);
  }
  .card {
    position: relative;
    width: 1200px;
    height: 686px;
    overflow: hidden;
  }
  .card-art {
    position: absolute;
    inset: 0;
  }
  .holder-name {
    position: absolute;
    left: 229px;
    top: 22px;
    margin: 0;
    font-family: "Marcellus", serif;
    font-weight: 400;
    font-size: 47px;
    letter-spacing: 1px;
    color: var(--ink-light);
    text-shadow: 2px 3px 4px rgba(20, 40, 80, 0.55);
  }
  .holder-title {
    position: absolute;
    left: 320px;
    top: 81px;
    margin: 0;
    font-family: "Source Sans 3", sans-serif;
    font-weight: 500;
    font-size: 25px;
    color: var(--navy);
  }
  .contact {
    position: absolute;
    margin: 0;
    font-family: "Gelasio", serif;
    font-weight: 600;
    color: var(--ink-light);
    text-shadow: 2px 3px 4px rgba(20, 40, 80, 0.55);
    line-height: 1.3;
    white-space: nowrap;
  }
  .contact-phone { left: 537px; top: 204px; font-size: 34px; }
  .contact-web { left: 535px; top: 354px; font-size: 35px; }
  .contact-mail { left: 468px; top: 482px; font-size: 34px; }
  .contact-address { left: 349px; top: 568px; font-size: 30px; line-height: 1.32; }
  .brand-name {
    position: absolute;
    left: 900px;
    top: 230px;
    margin: 0;
    font-family: "Gelasio", serif;
    font-weight: 600;
    font-size: 56px;
    letter-spacing: 2px;
    color: var(--ink-light);
  }
</style>
</head>
<body>
<div class="card">
  <svg class="card-art" width="1200" height="686" viewBox="0 0 1200 686" xmlns="http://www.w3.org/2000/svg">
    <defs>
      <linearGradient id="field" x1="0" y1="0" x2="1" y2="1">
        <stop offset="0" stop-color="#5b8fd0"/>
        <stop offset="0.55" stop-color="#4d86cf"/>
        <stop offset="1" stop-color="#3f78c4"/>
      </linearGradient>
      <radialGradient id="portraitTone" cx="0.5" cy="0.45" r="0.6">
        <stop offset="0" stop-color="#c9a98e"/>
        <stop offset="0.55" stop-color="#4b7fc6"/>
        <stop offset="1" stop-color="#2f62ad"/>
      </radialGradient>
      <linearGradient id="iconFill" x1="0" y1="0" x2="0" y2="1">
        <stop offset="0" stop-color="#dbe7f5"/>
        <stop offset="1" stop-color="#8fb3da"/>
      </linearGradient>
    </defs>

    <rect class="field" width="1200" height="686" fill="url(#field)"/>
    <g class="field-stripes" fill="#ffffff">
      <polygon points="560,0 700,0 1200,520 1200,686 1130,686" opacity="0.06"/>
      <polygon points="780,0 860,0 1200,360 1200,440" opacity="0.07"/>
      <polygon points="940,0 1060,0 1200,150 1200,270" opacity="0.06"/>
      <polygon points="330,0 420,0 1050,686 960,686" opacity="0.04"/>
    </g>

    <circle class="edge-band" cx="-457" cy="343" r="800" fill="var(--band)"/>
    <circle class="side-panel" cx="-457" cy="343" r="772" fill="var(--paper)"/>

    <circle class="portrait-ring" cx="194" cy="326" r="218" fill="var(--sky)"/>
    <circle class="portrait-frame" cx="194" cy="326" r="207" fill="#ffffff"/>
    <circle class="portrait" cx="194" cy="326" r="194" fill="url(#portraitTone)" role="img" aria-label="Portrait photo of Odessa Pruitt"/>

    <g class="icon icon-phone">
      <circle cx="465" cy="251" r="44" fill="url(#iconFill)" stroke="#e6eef8" stroke-width="4"/>
      <path d="M449 229 l9 -3 l7 14 l-6 5 q4 10 13 16 l6 -5 l13 8 l-3 9 q-4 4 -10 3 q-20 -6 -31 -28 q-3 -11 2 -19z" fill="var(--azure)"/>
      <path d="M474 233 q8 2 10 11 M476 224 q15 3 17 19" stroke="var(--azure)" stroke-width="3" fill="none" stroke-linecap="round"/>
    </g>

    <g class="icon icon-web" fill="none" stroke="var(--azure)" stroke-width="3">
      <circle cx="470" cy="381" r="44" fill="url(#iconFill)" stroke="#e6eef8" stroke-width="4"/>
      <circle cx="470" cy="381" r="24"/>
      <ellipse cx="470" cy="381" rx="10" ry="24"/>
      <line x1="446" y1="381" x2="494" y2="381"/>
      <path d="M450 369 h40 M450 393 h40"/>
    </g>

    <g class="icon icon-mail">
      <circle cx="401" cy="504" r="44" fill="url(#iconFill)" stroke="#e6eef8" stroke-width="4"/>
      <rect x="375" y="488" width="52" height="34" rx="2" fill="var(--azure)"/>
      <path d="M377 490 l24 18 l24 -18" stroke="#dbe7f5" stroke-width="2.5" fill="none"/>
    </g>

    <g class="icon icon-pin">
      <circle cx="286" cy="597" r="44" fill="url(#iconFill)" stroke="#e6eef8" stroke-width="4"/>
      <path d="M286 624 q-18 -22 -18 -36 a18 18 0 0 1 36 0 q0 14 -18 36z" fill="var(--azure)"/>
      <circle cx="286" cy="587" r="7" fill="#dbe7f5"/>
    </g>
  </svg>

  <p class="brand-name">MLGP</p>

  <h1 class="holder-name">Odessa Pruitt</h1>
  <p class="holder-title">Education Specialist</p>

  <p class="contact contact-phone">616-555-0148<br>629-555-0172</p>
  <p class="contact contact-web">www.Mlgpedu.example</p>
  <p class="contact contact-mail">pruittodessa@mailbox.example</p>
  <p class="contact contact-address">5073 Cormorant ridge<br>Dr. Nashville, TN 37940</p>
</div>
</body>
</html>
```